Ostrel Appraisals BV business cards (a financial services company)

I am looking for a business card design that stands out in the financial advisory field of business & intellectual property valuation. The business card design should be conservative, yet different. Address details have changed since the attached business card. New address is:

Molenvlietkade 27
4817 KT Leiden
The Netherlands

Telephone number remains the same.

```html
<!DOCTYPE html>
<html lang="en">
<head>
<meta charset="utf-8">
<title>Ostrel Appraisals BV – Business Card</title>
<link rel="stylesheet" href="https://fonts.googleapis.com/css2?family=Roboto:wght@400;500&family=Roboto+Condensed:wght@700&family=Montserrat:wght@600&display=swap">
<style>
  :root {
    --stage: #1e1e1e;
    --card-white: #ffffff;
    --band-grey: #777777;
    --swoosh-grey: #6a6a6a;
    --logo-grey: #666666;
    --tagline-grey: #6e6e6e;
    --text-light: #ffffff;
    --back-light: #8a8a8a;
    --back-dark: #5f5f5f;
  }
  * { box-sizing: border-box; margin: 0; padding: 0; }
  html, body { width: 1133px; height: 1200px; overflow: hidden; }
  body { background: var(--stage); position: relative; font-family: "Roboto", sans-serif; }

  .card { position: absolute; overflow: hidden; }
  .card-front { left: 213px; top: 149px; width: 707px; height: 404px; background: var(--card-white); }
  .card-back { left: 216px; top: 647px; width: 698px; height: 399px;
    background: linear-gradient(90deg, var(--back-dark) 0%, var(--back-light) 50%, var(--back-dark) 100%); }

  .wave { position: absolute; left: 0; top: 0; width: 707px; height: 404px; }

  .brand-name { position: absolute; left: 0; width: 362px; top: 122px; text-align: center;
    font-family: "Roboto", sans-serif; font-weight: 400; font-size: 30px; color: var(--logo-grey); letter-spacing: 0.5px; }
  .tagline { position: absolute; left: 0; width: 362px; top: 170px; text-align: center;
    font-family: "Montserrat", sans-serif; font-weight: 600; font-size: 13.5px; line-height: 19px;
    color: var(--tagline-grey); letter-spacing: 0.6px; }

  .address { position: absolute; left: 35px; top: 315px; color: var(--text-light);
    font-size: 17px; line-height: 21.5px; }

  .person { position: absolute; right: 36px; top: 256px; text-align: right; color: var(--text-light); }
  .person-name { font-family: "Roboto Condensed", sans-serif; font-weight: 700; font-size: 25px; line-height: 30px; }
  .person-name .credentials { font-size: 17px; }
  .person-role { font-size: 17px; font-weight: 500; line-height: 20px; }

  .contacts { position: absolute; right: 36px; top: 315px; list-style: none; color: var(--text-light); }
  .contacts li { display: flex; justify-content: flex-end; align-items: center; gap: 8px;
    font-size: 17px; line-height: 22px; }
  .contacts svg { width: 15px; height: 15px; fill: var(--text-light); }
</style>
</head>
<body>
  <section class="card card-front" aria-label="Business card front">
    <svg class="wave" viewBox="0 0 707 404" aria-hidden="true">
      <path d="M0 246 C120 292 260 290 430 255 C560 226 650 210 707 236 L707 404 L0 404 Z" fill="var(--band-grey)"/>
      <path d="M0 241 C130 292 270 285 430 248 C580 214 660 196 707 236" fill="none" stroke="var(--card-white)" stroke-width="7"/>
      <path d="M0 237 C140 285 280 278 430 242 C580 206 660 186 707 232" fill="none" stroke="var(--swoosh-grey)" stroke-width="4"/>
    </svg>

    <div class="brand-name">OSTREL APPRAISALS</div>
    <div class="tagline">BUSINESS AND INTELLECTUAL<br>PROPERTY VALUATIONS</div>

    <address class="address" style="font-style:normal">
      Molenvlietkade 27<br>4817 KT Leiden<br>The Netherlands
    </address>

    <div class="person">
      <div class="person-name">Maarten Velde, <span class="credentials">CFA, ASA, RV</span></div>
      <div class="person-role">Managing Director</div>
    </div>

    <ul class="contacts">
      <li>+31(0)70 555 0142
        <svg viewBox="0 0 24 24" aria-hidden="true"><path d="M6.6 10.8a15 15 0 0 0 6.6 6.6l2.2-2.2a1 1 0 0 1 1-.25 11.4 11.4 0 0 0 3.6.57 1 1 0 0 1 1 1V20a1 1 0 0 1-1 1A17 17 0 0 1 3 4a1 1 0 0 1 1-1h3.5a1 1 0 0 1 1 1c0 1.25.2 2.45.57 3.57a1 1 0 0 1-.25 1z"/></svg>
      </li>
      <li>mvelde@ostrelappraisals.com
        <svg viewBox="0 0 24 24" aria-hidden="true"><path d="M2 5h20v14H2z M3 6l9 7 9-7" fill="var(--text-light)" stroke="var(--band-grey)" stroke-width="1.5"/></svg>
      </li>
      <li>www.ostrelappraisals.com
        <svg viewBox="0 0 24 24" aria-hidden="true"><circle cx="12" cy="12" r="10"/><path d="M8 6c2 1 3 3 1 5s1 4 3 3 2 3 0 5M15 4c-1 2 1 3 3 3" fill="none" stroke="var(--band-grey)" stroke-width="2"/></svg>
      </li>
    </ul>
  </section>

  <section class="card card-back" role="img" aria-label="Card back: embossed repeating brand monogram pattern on silver-grey"></section>
</body>
</html>
```